Quality Improvement Software for healthcare agencies needs a website.

VORTEL218 is a software for hospices and home health agencies to manage their Quality Assurance Performance Improvement programs to remain complaint with the standards set by Sanavox and the Bureau of Clinical Oversight. The web accessible software-as-a-service provides an easy, turn-key way for agencies to organize all the information they need to manage and track.

Coding

Coded - Design and coding required

Number of Pages Required

4 page

```html
<!DOCTYPE html>
<html lang="en">
<head>
<meta charset="utf-8">
<title>VORTEL218 – Quality Improvement Software</title>
<link href="https://fonts.googleapis.com/css2?family=Montserrat:ital,wght@0,400;0,500;0,600;0,700;1,700&display=swap" rel="stylesheet">
<style>
:root{
  --orange:#f7941d;
  --ink:#1c1c1c;
  --text:#333;
  --cream:#fdf5ec;
  --navy:#0a3d5e;
  --navy-deep:#072a45;
  --brown:#2b1a0c;
  --footer:#1d1d1d;
  --blue:#2a8fd6;
  --green:#3cb44a;
  --yellow:#f6c21c;
  --white:#fff;
}
*{margin:0;padding:0;box-sizing:border-box}
html,body{width:1200px;height:4511px;overflow:hidden}
body{font-family:"Montserrat",sans-serif;color:var(--text);background:var(--white);position:relative}
section,header,footer{position:absolute;left:0;width:1200px}
.accent{color:var(--orange)}
.brand{font-weight:700;color:var(--ink);font-size:27px;letter-spacing:.5px;display:flex;align-items:center;gap:8px}
.brand .dot{width:20px;height:20px;background:var(--orange)}
.btn{position:absolute;background:var(--orange);color:var(--white);font-size:13px;font-weight:600;display:flex;align-items:center;justify-content:center}
.bar{display:flex;gap:3px;margin-top:8px}
.bar i{width:6px;height:5px;display:block}
.bar i:nth-child(1){background:var(--blue)}
.bar i:nth-child(2){background:var(--green)}
.bar i:nth-child(3){background:var(--yellow)}
.bar i:nth-child(4){background:var(--orange)}
.bar.center{justify-content:center}
h2{font-size:31px;font-weight:600;color:var(--ink);line-height:1.2}
h3{font-size:25px;font-weight:600;color:var(--ink)}
p.body{font-size:12.5px;line-height:1.65;color:var(--text)}
.photo{position:absolute}

/* header */
.site-header{top:0;height:68px;background:var(--white)}
.site-header .brand{position:absolute;left:140px;top:18px}
.nav{position:absolute;left:487px;top:25px;display:flex;gap:28px;font-size:14px;color:var(--ink)}
.nav .active{color:var(--orange)}

/* hero */
.hero{top:68px;height:565px;background:linear-gradient(90deg,#3a6d8c 0%,#0f4a70 45%,var(--navy-deep) 100%)}
.hero .photo{left:0;top:0;width:560px;height:565px;background:radial-gradient(circle at 45% 45%,#6fc2e6 0%,#2b6f94 35%,rgba(15,74,112,0) 75%)}
.hero-title{position:absolute;right:141px;top:122px;width:640px;text-align:right;color:var(--white);font-size:32px;font-weight:600;line-height:1.2}
.hero-title em{font-style:italic;font-weight:700;color:var(--orange)}
.hero .btn{left:855px;top:395px;width:204px;height:39px}

/* about */
.about{top:633px;height:537px}
.about .frame{position:absolute;left:150px;top:95px;width:415px;height:352px;background:var(--orange)}
.about .photo{left:140px;top:85px;width:418px;height:352px;background:linear-gradient(135deg,#e7b96b,#d7d9dc 50%,#8aa5b8)}
.about .text{position:absolute;left:641px;top:105px;width:420px}
.about .text p{margin-top:18px}
.about .btn{left:641px;top:370px;width:118px;height:38px}

/* features */
.features{top:1170px;height:1825px;background:var(--cream)}
.features .heading{position:absolute;top:72px;left:0;width:1200px;text-align:center}
.feature-img{position:absolute;width:417px;height:353px}
.feature-text{position:absolute;width:410px}
.feature-text p{margin-top:24px}

/* commitment */
.commit{top:2995px;height:520px;background:var(--brown)}
.commit .text{position:absolute;left:140px;top:110px;width:420px;color:var(--white)}
.commit h2{color:var(--white)}
.commit p{color:var(--white);font-size:13.5px;line-height:1.7;margin-top:20px;font-weight:500}
.commit .btn{left:140px;top:368px;width:205px;height:37px}
.commit .photo{left:642px;top:85px;width:416px;height:352px;background:linear-gradient(135deg,#6d8294,#334a5c 60%,#1d2c38)}

/* testimonials */
.customers{top:3515px;height:535px;background:var(--white)}
.customers .heading{position:absolute;top:85px;left:0;width:1200px;text-align:center}
.card{position:absolute;top:170px;width:285px;height:290px;background:var(--white);box-shadow:0 4px 18px rgba(0,0,0,.08);text-align:center;padding:30px 25px}
.avatar{width:52px;height:52px;border-radius:50%;margin:0 auto;background:linear-gradient(#f2c9a8,#a0653e)}
.card h4{font-size:12.5px;font-weight:600;color:var(--ink);margin-top:16px}
.stars{color:var(--yellow);font-size:13px;letter-spacing:2px;margin-top:8px}
.card p{font-size:12px;line-height:1.7;margin-top:12px;color:var(--text)}
.arrow{position:absolute;top:297px;width:34px;height:34px;display:flex;align-items:center;justify-content:center}
.arrow.prev{left:78px;border:1.5px solid var(--ink)}
.arrow.next{left:1088px;background:var(--orange)}

/* footer */
.site-footer{top:4050px;height:461px;background:linear-gradient(180deg,#252525,var(--footer))}
.site-footer .brand{position:absolute;left:140px;top:100px;color:var(--white);font-size:33px}
.footer-about{position:absolute;left:140px;top:168px;width:230px;font-size:12.5px;line-height:1.7;color:#e6e6e6}
.social{position:absolute;left:140px;top:305px;display:flex;gap:13px}
.social span{width:36px;height:32px;background:var(--orange);display:block}
.col-title{font-size:14px;font-weight:600;color:var(--white)}
.links{position:absolute;left:571px;top:110px}
.links ul{list-style:none;margin-top:30px}
.links li{font-size:12.5px;color:#e6e6e6;margin-bottom:15px}
.links li.active{color:var(--orange)}
.contact{position:absolute;left:888px;top:110px;width:180px}
.contact .row{display:flex;gap:14px;align-items:center;position:absolute;left:0;font-size:12.5px;color:#e6e6e6;line-height:1.5}
.contact .ico{width:32px;height:32px;background:var(--orange);flex:none;display:flex;align-items:center;justify-content:center}
.bottom{position:absolute;left:140px;top:415px;width:918px;border-top:1px solid #444;padding-top:15px;display:flex;justify-content:space-between;font-size:12px;color:#e6e6e6}
</style>
</head>
<body>

<header class="site-header">
  <div class="brand"><span class="dot"></span>VORTEL218</div>
  <nav class="nav">
    <span class="active">Home</span><span>About Us</span><span>Features</span><span>Pricing</span><span>Testimonials</span>
  </nav>
  <div class="btn" style="left:940px;top:16px;width:118px;height:38px">Contact Us</div>
</header>

<section class="hero">
  <div class="photo" role="img" aria-label="Doctor holding a glowing medical cross hologram"></div>
  <h1 class="hero-title">Welcome to <span class="accent">VORTEL218</span>, your<br>one-stop solution for<br>managing and tracking<br>your <em>Quality Assurance</em><br><em>Performance Improvement</em><br>(<span class="accent">QAPI</span>) programs.</h1>
  <div class="btn">Sign Up For A Free Trial</div>
</section>

<section class="about">
  <div class="frame"></div>
  <div class="photo" role="img" aria-label="Tablet showing software and database screens on a desk"></div>
  <div class="text">
    <h2>About <span class="accent">VORTEL218</span></h2>
    <div class="bar"><i></i><i></i><i></i><i></i></div>
    <p class="body">Our web-accessible software-as-a-service is designed to simplify the process of remaining compliant with Sanavox and Bureau of Clinical Oversight standards.</p>
    <p class="body">At VORTEL218, we understand the importance of organizing all the necessary information in one place. That's why our software provides an easy and turn-key way for hospices and home health agencies to manage and track their QAPI programs.</p>
  </div>
  <div class="btn">Read More</div>
</section>

<section class="features">
  <div class="heading">
    <h2>Some Of The Key Features<br>Of <span class="accent">VORTEL218</span> Include</h2>
    <div class="bar center"><i></i><i></i><i></i><i></i></div>
  </div>

  <div class="feature-img" style="left:140px;top:200px;background:#5d7185" role="img" aria-label="Dashboard screen with charts and metrics"></div>
  <div class="feature-text" style="left:630px;top:295px">
    <h3>Customizable Dashboards</h3>
    <div class="bar"><i></i><i></i><i></i><i></i></div>
    <p class="body">Our software allows agencies to create customized dashboards that provide a real-time view of their <b>QAPI</b> program's progress. This feature enables agencies to easily monitor and track performance metrics, identify areas for improvement, and take corrective action as needed.</p>
  </div>

  <div class="feature-img" style="left:642px;top:596px;background:linear-gradient(135deg,#8c9aa6,#3b4650)" role="img" aria-label="Businessman holding a tablet with workflow icons"></div>
  <div class="feature-text" style="left:140px;top:690px">
    <h3>Automated Workflows</h3>
    <div class="bar"><i></i><i></i><i></i><i></i></div>
    <p class="body"><b>VORTEL218</b> automates many of the manual processes involved in <b>QAPI</b> program management, such as assigning tasks, setting deadlines, and generating reports. This feature ensures that tasks are completed on time and helps agencies stay organized and efficient.</p>
  </div>

  <div class="feature-img" style="left:140px;top:990px;background:linear-gradient(135deg,#c9ccc8,#6b6e6a)" role="img" aria-label="Team collaborating around a laptop in an office"></div>
  <div class="feature-text" style="left:630px;top:1083px">
    <h3>Collaborative Communication</h3>
    <div class="bar"><i></i><i></i><i></i><i></i></div>
    <p class="body">Our software facilitates collaboration and communication between team members by providing a centralized platform for sharing information, documents, and feedback. This feature helps ensure that everyone is working towards the same goals and objectives.</p>
  </div>

  <div class="feature-img" style="left:642px;top:1386px;background:linear-gradient(135deg,#dfe4e8,#8e9aa4)" role="img" aria-label="Colleagues reviewing reports on a laptop"></div>
  <div class="feature-text" style="left:140px;top:1468px">
    <h3>Comprehensive Reporting</h3>
    <div class="bar"><i></i><i></i><i></i><i></i></div>
    <p class="body"><b>VORTEL218</b> generates detailed reports that provide insights into performance trends, identify areas for improvement, and help agencies demonstrate compliance with Sanavox and Bureau of Clinical Oversight standards. This feature allows agencies to make data-driven decisions and continuously improve their <b>QAPI</b> programs.</p>
  </div>
</section>

<section class="commit">
  <div class="text">
    <h2>At <span class="accent">VORTEL218</span></h2>
    <div class="bar"><i></i><i></i><i></i><i></i></div>
    <p>At VORTEL218, we are committed to providing our clients with the best possible software solution for managing their <b>QAPI</b> programs. Our software is designed to be intuitive, user-friendly, and customizable to meet the unique needs of each agency. If you have any questions or would like to learn more about our software, please don't hesitate to contact us today!</p>
  </div>
  <div class="btn">Sign Up For A Free Trial</div>
  <div class="photo" role="img" aria-label="Medical professionals framed by bar chart outlines"></div>
</section>

<section class="customers">
  <div class="heading">
    <h2>Our Satisfied <span class="accent">Customers</span></h2>
    <div class="bar center"><i></i><i></i><i></i><i></i></div>
  </div>
  <div class="arrow prev"><svg width="18" height="12" viewBox="0 0 18 12"><path d="M17 6H2M6 1 1 6l5 5" fill="none" stroke="#1c1c1c" stroke-width="1.5"/></svg></div>
  <div class="card" style="left:140px">
    <div class="avatar" role="img" aria-label="Customer portrait"></div>
    <h4>Arlen Fisk</h4><div class="stars">★★★★★</div>
    <p>Standard dummy text ever since the 1500s, when an unknown printer took a galley of type and scrambled it to make a type specimen book. It has survived not only five centuries.</p>
  </div>
  <div class="card" style="left:457px">
    <div class="avatar" role="img" aria-label="Customer portrait"></div>
    <h4>Tessa Moravec</h4><div class="stars">★★★★★</div>
    <p>Standard dummy text ever since the 1500s, when an unknown printer took a galley of type and scrambled it to make a type specimen book. It has survived not only five centuries.</p>
  </div>
  <div class="card" style="left:773px">
    <div class="avatar" role="img" aria-label="Customer portrait"></div>
    <h4>Lina Quarry</h4><div class="stars">★★★★★</div>
    <p>Standard dummy text ever since the 1500s, when an unknown printer took a galley of type and scrambled it to make a type specimen book. It has survived not only five centuries.</p>
  </div>
  <div class="arrow next"><svg width="18" height="12" viewBox="0 0 18 12"><path d="M1 6h15M12 1l5 5-5 5" fill="none" stroke="#fff" stroke-width="1.5"/></svg></div>
</section>

<footer class="site-footer">
  <div class="brand"><span class="dot"></span>VORTEL218</div>
  <p class="footer-about">Lorem ipsum dolor sit amet, consectetur adipiscing elit, sed do eiusmod tempor incididunt ut labore et dolore magna aliqua. Ut enim ad minim veniam.</p>
  <div class="social"><span></span><span></span><span></span><span></span></div>
  <div class="links">
    <div class="col-title">Quick Links</div>
    <div class="bar"><i></i><i></i><i></i><i></i></div>
    <ul><li class="active">Home</li><li>About Us</li><li>Features</li><li>Pricing</li><li>Testimonials</li><li>Contact Us</li></ul>
  </div>
  <div class="contact">
    <div class="col-title">Contact Us</div>
    <div class="bar"><i></i><i></i><i></i><i></i></div>
    <div class="row" style="top:58px"><span class="ico"><svg width="14" height="18" viewBox="0 0 14 18"><path d="M7 1a6 6 0 0 0-6 6c0 4.5 6 10 6 10s6-5.5 6-10a6 6 0 0 0-6-6z" fill="#fff"/><circle cx="7" cy="7" r="2.2" fill="#f7941d"/></svg></span><span>123, Lorem ipsum<br>dolor sit amet,</span></div>
    <div class="row" style="top:118px"><span class="ico"><svg width="16" height="16" viewBox="0 0 16 16"><path d="M3 1l3 3-2 2c1 2 3 4 5 5l2-2 3 3-2 3C7 15 1 9 1 3z" fill="#fff"/></svg></span><span style="font-size:14px">123 456 7890</span></div>
    <div class="row" style="top:172px"><span class="ico"><svg width="16" height="12" viewBox="0 0 16 12"><rect x="1" y="1" width="14" height="10" fill="#fff"/><path d="M1 1l7 6 7-6" fill="none" stroke="#f7941d" stroke-width="1.3"/></svg></span><span>info@vortel218.com</span></div>
  </div>
  <div class="bottom"><span>Copyright © 2023 <b>VORTEL218</b>. All Rights Reserved.</span><span>Privacy Policy | Terms &amp; Conditions</span></div>
</footer>

</body>
</html>
```